Vantor Burnished Concrete & Grinding
I'm looking for a business card and logo design for my
new Polished Concrete & Grinding business,
If you were to look up Vantor in the dictionary it would
say, first in importance, order, or position; leading.
Polished Concrete floors are a niche market, that are being used currently in Shopping centres, office spaces and by most high end architects, builders and designers.
i need my business card & logo to stand out from my
competitors, i need my design + logo to reflect this it
needs to be simple, professional, eye catching, easy
to read and scream quality. The logo will need to be
suitable for a whole range of applications including,
uniforms, letter heads, stickers, and eventually
incorporating in vehicle vinyl wrapping.
Target Market(s)
Builders, architects, Interior designers & home owners
Contact Information for Business Card
Front side:
- Vantor Burnished Concrete & Grinding.
- Logo
Rear side:
- Liam Verhorst
- 0481736502
- info@vantorbcg.com.au
- commercial - domestic - industrial
- (later down the line website & space for
social media links
www.vantorburnishedconcrete.com.au)
Colors
Designer to choose colors to be used in the design.
Look and feel

```html
<!DOCTYPE html>
<html lang="en">
<head>
<meta charset="utf-8">
<title>Vantor Burnished Concrete &amp; Grinding — Business Card</title>
<link rel="stylesheet" href="https://fonts.googleapis.com/css2?family=Work+Sans:wght@400;500&display=swap">
<style>
  :root {
    --backdrop: #efefee;
    --card: #e4e3e1;
    --copper: #a87a58;
    --mark-light: #f7f6f4;
    --photo-warm: #d9b79a;
    --photo-wall: #e8e2da;
    --photo-floor: #8d918c;
  }
  * { margin: 0; padding: 0; box-sizing: border-box; }
  html, body {
    width: 1200px; height: 892px; overflow: hidden;
    background: var(--backdrop);
    font-family: "Work Sans", Arial, sans-serif;
  }
  .sheet {
    position: relative; width: 1200px; height: 892px;
    display: flex; justify-content: center; align-items: center; gap: 80px;
  }
  .card {
    position: relative; width: 340px; height: 556px;
    background: var(--card); overflow: hidden;
    box-shadow: 0 2px 10px rgba(0,0,0,0.06);
  }

  /* Contact side */
  .card-photo { position: absolute; inset: 0; width: 100%; height: 100%; }
  .card-wordmark {
    position: absolute; left: 84px; top: 62px;
    color: var(--mark-light); font-size: 13px; letter-spacing: 0.22em;
    line-height: 1.15; text-transform: uppercase;
  }
  .card-wordmark span { display: block; }
  .card-wordmark .w2 { padding-left: 10px; }
  .card-wordmark .w3 { padding-left: 4px; }
  .card-wordmark .w4 { padding-left: 14px; }
  .holder-name {
    position: absolute; left: 40px; top: 205px;
    color: var(--copper); font-size: 21px; font-weight: 500; letter-spacing: 0.08em;
  }
  .contact {
    position: absolute; left: 40px;
    color: var(--copper); font-size: 11px; letter-spacing: 0.24em;
    line-height: 1.35; text-transform: uppercase;
  }
  .contact span { display: block; }
  .contact-phone { top: 250px; }
  .contact-email { top: 290px; }
  .contact-web { top: 338px; }
  .contact-web .l2 { padding-left: 12px; }
  .contact-web .l3 { padding-left: 24px; }
  .contact-web .l4 { padding-left: 10px; }
  .contact-web .l5 { padding-left: 20px; }

  /* Brand side */
  .brand-name {
    position: absolute; left: 0; right: 0; top: 150px; text-align: center;
    color: var(--copper); font-size: 48px; font-weight: 400; letter-spacing: 0.14em;
    text-transform: uppercase;
  }
  .brand-descriptor {
    position: absolute; left: 110px; top: 290px;
    color: var(--copper); font-size: 17px; letter-spacing: 0.3em;
    line-height: 1.25; text-transform: uppercase;
  }
  .brand-descriptor span { display: block; }
  .brand-descriptor .d2 { padding-left: 6px; }
  .brand-descriptor .d3 { padding-left: 2px; }
  .brand-descriptor .d4 { padding-left: 12px; }
  .brand-web {
    position: absolute; left: 18px; right: 18px; bottom: 26px; text-align: center;
    color: #8f8c88; font-size: 9.5px; letter-spacing: 0.26em; text-transform: uppercase;
  }
</style>
</head>
<body>
  <main class="sheet">
    <section class="card card-contact">
      <svg class="card-photo" viewBox="0 0 340 556" role="img" aria-label="Photograph of a polished concrete interior with a chair and framed artwork">
        <defs>
          <linearGradient id="photo-tone" x1="0" y1="0" x2="0" y2="1">
            <stop offset="0" stop-color="var(--photo-warm)"/>
            <stop offset="0.45" stop-color="var(--photo-wall)"/>
            <stop offset="0.7" stop-color="#c9c4bd"/>
            <stop offset="1" stop-color="var(--photo-floor)"/>
          </linearGradient>
        </defs>
        <polygon points="255,0 340,0 340,556 155,556" fill="url(#photo-tone)"/>
      </svg>
      <div class="card-wordmark">
        <span class="w1">Vantor</span>
        <span class="w2">Burnished</span>
        <span class="w3">Concrete &amp;</span>
        <span class="w4">Grinding</span>
      </div>
      <p class="holder-name">Liam Verhorst</p>
      <p class="contact contact-phone">048 173 65 02</p>
      <p class="contact contact-email"><span>info@vantorbcg</span><span>.com.au</span></p>
      <p class="contact contact-web">
        <span class="l1">www.</span>
        <span class="l2">vantor</span>
        <span class="l3">burnished</span>
        <span class="l4">concrete</span>
        <span class="l5">.com.au</span>
      </p>
    </section>

    <section class="card card-brand">
      <p class="brand-name">Vantor</p>
      <p class="brand-descriptor">
        <span class="d1">Vantor</span>
        <span class="d2">Burnished</span>
        <span class="d3">Concrete &amp;</span>
        <span class="d4">Grinding</span>
      </p>
      <p class="brand-web">www.vantorburnishedconcrete.com.au</p>
    </section>
  </main>
</body>
</html>
```